Flyer-Design für ein kleines Familienunternehmen
Zielgruppe
Wir sind ein kleines Familienunternehmen, welche gewerbliche Kaffeemaschinen verkauft und den service darum anbietet.
Unsere Homepage: https://www.morgenbohne-handel.de/
Wir möchten eine neue Zielgruppe erschließen.
Die neue Zielgruppe sind Büros.
Angebot ist : - Service
- Kaffee Lieferung
- Rund um Paket
Aufgabenstellung
Merkmal der Familienunternehmen und Regionalität soll deutlich werden.
Wir Bieten: schnelle; einfache; individuelle Lösung
Rund um Sorglos.

```html
<!DOCTYPE html>
<html lang="de">
<head>
<meta charset="utf-8">
<title>Morgenbohne – Flyer</title>
<link href="https://fonts.googleapis.com/css2?family=Kaushan+Script&family=Open+Sans:wght@300;400;600&family=Quicksand:wght@500&display=swap" rel="stylesheet">
<style>
:root{
  --brown:#4a2511;
  --mint:#a9d9bb;
  --text:#5a5a5a;
  --paper:#ffffff;
  --stage:#e4e2df;
  --photo-office-a:#c9c3bb;
  --photo-office-b:#6d7a86;
  --photo-coffee-a:#5a4636;
  --photo-coffee-b:#2f2a27;
  --photo-team-a:#8e8f8d;
  --photo-team-b:#4a4b4c;
}
*{margin:0;padding:0;box-sizing:border-box}
html,body{width:1200px;height:1200px;overflow:hidden;background:var(--stage)}
body{position:relative;font-family:'Open Sans',sans-serif;font-weight:300;color:var(--text)}
.panel{position:absolute;background:var(--paper);overflow:hidden;box-shadow:0 2px 8px rgba(0,0,0,.15)}
.photo{position:absolute;left:0;top:0;width:100%}
.band{position:absolute;left:0;width:100%;height:12px;background:var(--mint)}
.script{font-family:'Kaushan Script',cursive;color:var(--brown);font-weight:400}
.abs{position:absolute}
.badge{position:absolute;border-radius:50%;background:var(--paper);display:flex;align-items:center;justify-content:center;text-align:center}
.brand-name{font-family:'Open Sans',sans-serif;font-weight:600;color:var(--brown);font-size:30px}
.badge-services{font-family:'Quicksand',sans-serif;font-weight:500;color:var(--brown);font-size:19px;line-height:1.2}
.white{color:#fff}
.small{font-size:12px;line-height:1.45}
.body-copy{font-size:13.5px;line-height:1.5}
b,.strong{font-weight:600}
</style>
</head>
<body>

<!-- Cover -->
<section class="panel cover" style="left:10px;top:10px;width:585px;height:585px">
  <div class="photo" role="img" aria-label="Foto: lächelnde Frau mit Kaffeetasse in einem hellen Büro" style="height:352px;background:linear-gradient(120deg,var(--photo-office-a),var(--photo-office-b))"></div>
  <div class="band" style="top:352px"></div>
  <div class="badge" style="left:50px;top:165px;width:222px;height:222px"><span class="brand-name">Morgenbohne</span></div>
  <h1 class="script abs" style="left:46px;top:388px;font-size:33px;line-height:52px">Den leckersten Kaffee im Veedel?<br>Den machst jetzt Du!</h1>
  <div class="abs" style="left:52px;top:513px;width:157px;height:3px;background:var(--mint)"></div>
  <p class="abs small" style="left:52px;top:518px"><span class="strong">Bio - Fairtrade - Regional</span><br>Morgenbohne by Brandauer Kaffeemaschinen e.K.</p>
</section>

<!-- Back -->
<section class="panel back" style="left:605px;top:10px;width:585px;height:585px">
  <h2 class="script abs" style="left:0;width:100%;text-align:center;top:28px;font-size:19px">Wir bieten einfache Lösungen für Deinen Kaffee im Büro:</h2>
  <p class="abs" style="left:0;width:100%;text-align:center;top:72px;font-size:11px;font-weight:400;color:#333">Individuelle Beratung - Gute Maschinen - Leckeren Kaffee - perfekten Service</p>
  <div class="photo" role="img" aria-label="Foto: vier Männer der Familie hinter einer Siebträgermaschine" style="top:115px;height:236px;background:linear-gradient(180deg,var(--photo-team-a),var(--photo-team-b))"></div>
  <div class="band" style="top:351px"></div>
  <p class="abs" style="left:0;width:100%;text-align:center;top:378px;font-size:11px">Familie Brandauer - <b style="color:var(--brown)">Jederzeit dein Ansprechpartner</b></p>
  <p class="abs" style="left:83px;top:425px;font-size:10.5px;line-height:1.4">Brandauer Kaffeemaschinen e.K.<br>Lindenallee 14<br>50170 Beispielstadt<br>Tel.: 0 22 00 / 12 345 67<br>Mail: office@morgenbohne-handel.de</p>
  <p class="abs" style="left:308px;top:425px;font-size:10.5px;line-height:1.4">Öffnungszeiten Ladenlokal</p>
  <table class="abs" style="left:306px;top:454px;font-size:10.5px;line-height:1.4;border-collapse:collapse">
    <tr><td style="padding-right:10px">Montag bis Donnerstag:</td><td>09:00 – 17:00 Uhr</td></tr>
    <tr><td>Freitag:</td><td>09:00 – 15:00 Uhr</td></tr>
    <tr><td>Samstag:</td><td>nach Vereinbarung</td></tr>
  </table>
  <p class="abs" style="left:0;width:100%;text-align:center;top:540px;font-size:23px;color:#777">www.morgenbohne-handel.de</p>
</section>

<!-- Inside left -->
<section class="panel inside-left" style="left:10px;top:605px;width:590px;height:585px">
  <div class="photo" role="img" aria-label="Foto: Cappuccino mit Latte Art und Gebäck auf einem Holzbrett" style="height:352px;background:linear-gradient(150deg,var(--photo-coffee-a),var(--photo-coffee-b))"></div>
  <h2 class="script abs white" style="left:38px;top:166px;font-size:38px;line-height:56px">Unsere Kompetenz<br>ist gelebte Praxis.</h2>
  <p class="abs white body-copy" style="left:38px;top:290px;font-size:14.5px">Wir sind seit Jahren in der Kaffeeszene unter-<br>wegs und wissen genau, worauf es ankommt.</p>
  <div class="band" style="top:352px"></div>
  <div class="badge badge-services" style="left:400px;top:268px;width:148px;height:148px">Service<br>Beratung<br>Verkauf</div>
  <p class="abs body-copy" style="left:62px;top:385px">Und das ist vor allem <b>gute Qualität</b>, denn:</p>
  <p class="abs body-copy" style="left:62px;top:410px"><b>Kaffee</b>…<br>… sorgt für ein angenehmes (Arbeits-) Klima.<br>… sorgt für ein entspanntes, kommunikatives und produktives Umfeld.<br>… beflügelt und mobilisiert.<br>… beruhigt und entspannt gleichzeitig.</p>
  <p class="script abs" style="left:62px;top:528px;font-size:18px">Ein leckerer Kaffee sollte daher immer verfügbar sein.</p>
</section>

<!-- Inside right -->
<section class="panel inside-right" style="left:600px;top:605px;width:590px;height:585px">
  <div class="photo" role="img" aria-label="Foto: zwei Männer arbeiten gemeinsam an einer Kaffeemaschine" style="height:352px;background:linear-gradient(135deg,var(--photo-team-a),var(--photo-team-b))"></div>
  <h2 class="script abs white" style="left:72px;top:166px;font-size:38px;line-height:56px">Genau für Deine<br>Anforderung!</h2>
  <p class="abs white body-copy" style="left:72px;top:290px;font-size:14.5px">Wir sind Dir bei der Auswahl Deiner Maschine behilflich.<br>Und auch danach sind wir jederzeit Dein Ansprechpartner.</p>
  <div class="band" style="top:352px"></div>
  <div class="abs small" style="left:35px;top:390px;width:300px"><b>Große Auswahl</b><br>Wir haben sehr unterschiedliche Geräte, verschiede-ne Hersteller und auch zahlreiche Kaffee´s für Dich im Angebot. Bei uns gibt´s kein Einerlei von der Stange. Für Deine Ansprüche und Wünsche ist sicher das Richtige dabei.</div>
  <div class="abs small" style="left:35px;top:503px;width:310px"><b>TOP Service!</b><br>Von der Beratung über Finanzierung, Kauf oder Miete bis hin zum technischen Support, stehen wir an Deiner Seite. Damit unsere Verbindung über Jahre hält.</div>
  <div class="abs small" style="left:370px;top:390px;width:200px"><b>Lokal</b><br>Wir sind nicht weit weg, sondern Dein netter Ansprechpartner direkt aus der Nähe.</div>
  <p class="script abs" style="left:390px;top:458px;font-size:28px">Besuch uns.</p>
  <p class="abs small" style="left:370px;top:502px;width:192px;text-align:right">Fass die Maschinen mal an.<br>Trink einen leckeren Kaffee.<br>Und entscheide dann.</p>
</section>

</body>
</html>
```